Bayfield Tools and Building Materials Inc. (Rebranding)

Target Market(s)

mainly people who do DIY, and also construction companies.

Industry/Entity Type

Construction

Contact Information for Business Card

418 R. Malvar St. Brgy. 512 San Lazaro Manila, Philippines 1003
(02) 846-1937
www.btm-ph.com
bayfieldtools@mailbay.com

Number of Pages Required

5+ page

Font styles to use
Sans Serif

Colors
f37122
f78f20

Requirements
Must have
• to RETAIN the current logo used.
Nice to have
• ideas on how to apply the current logos to different promotional items
Should not have
• DO NOT change the Current Logo

```html
<!DOCTYPE html>
<html lang="en">
<head>
<meta charset="utf-8">
<title>Bayfield Tools and Building Materials Inc. — Stationery</title>
<link rel="stylesheet" href="https://fonts.googleapis.com/css2?family=Arimo:wght@400;700&display=swap">
<style>
  :root {
    --brand: #f57110;
    --brand-light: #f78f20;
    --brand-dark: #e0650c;
    --paper: #ffffff;
    --ink-line: #8a8a8a;
    --backdrop: #efe7da;
    --ring: #3a3a3a;
  }
  * { box-sizing: border-box; margin: 0; padding: 0; }
  html, body { width: 1200px; height: 720px; overflow: hidden; }
  body {
    background: var(--backdrop);
    font-family: "Arimo", Arial, sans-serif;
    color: var(--paper);
    position: relative;
  }
  .sheet { position: absolute; background: var(--brand); }

  /* Wordmark */
  .wordmark { position: absolute; font-weight: 700; color: var(--paper); line-height: 1; text-transform: uppercase; white-space: nowrap; }
  .wordmark .name { display: block; letter-spacing: 0.01em; }
  .wordmark .sub { display: block; letter-spacing: 0.06em; margin-top: 2px; }

  /* Letterhead */
  .letterhead { left: 76px; top: 110px; width: 352px; height: 498px; }
  .letterhead .wordmark { left: 39px; top: 40px; }
  .letterhead .wordmark .name { font-size: 17px; }
  .letterhead .wordmark .sub { font-size: 3.4px; }
  .letter-body { position: absolute; left: 39px; top: 82px; width: 280px; font-size: 5.6px; line-height: 7.2px; }
  .letter-body p { margin-bottom: 7px; }
  .letter-body h3 { font-size: 5.6px; font-weight: 400; }
  .letter-footer { position: absolute; left: 46px; top: 459px; font-size: 5.6px; }

  /* Business cards */
  .card { top: 109px; width: 150px; height: 84px; }
  .card-front { left: 460px; }
  .card-front .wordmark { left: 42px; top: 34px; }
  .card-front .wordmark .name { font-size: 12px; }
  .card-front .wordmark .sub { font-size: 2.4px; margin-top: 1px; }
  .card-back { left: 650px; }
  .card-back .person { position: absolute; left: 10px; top: 12px; }
  .card-back .person-name { font-size: 8px; font-weight: 700; }
  .card-back .person-role { font-size: 4.2px; font-weight: 700; margin-top: 2px; }
  .card-back .wordmark { right: 6px; top: 32px; text-align: right; }
  .card-back .wordmark .name { font-size: 8.5px; }
  .card-back .wordmark .sub { font-size: 1.7px; margin-top: 1px; }
  .card-back .contact { position: absolute; left: 10px; top: 52px; font-size: 4.8px; font-weight: 700; line-height: 6.4px; list-style: none; }

  /* Envelopes */
  .envelope-front { left: 449px; top: 216px; width: 369px; height: 184px; }
  .envelope-front .wordmark { left: 25px; top: 82px; }
  .envelope-front .wordmark .name { font-size: 26px; }
  .envelope-front .wordmark .sub { font-size: 5px; margin-top: 3px; }
  .address-window { position: absolute; left: 186px; top: 78px; width: 150px; height: 74px; background: var(--paper); }
  .address-window svg { position: absolute; inset: 0; }
  .envelope-back { left: 448px; top: 421px; width: 369px; height: 183px; }
  .envelope-back svg { position: absolute; inset: 0; }

  /* Notepad */
  .notepad { left: 838px; top: 252px; width: 250px; height: 354px; border-left: 2px solid #fde7d6; }
  .notepad .wordmark { left: 76px; top: 130px; }
  .notepad .wordmark .name { font-size: 20px; }
  .notepad .wordmark .sub { font-size: 3.6px; }
  .spiral { position: absolute; left: 838px; top: 236px; width: 250px; height: 40px; }
</style>
</head>
<body>

  <section class="sheet letterhead" aria-label="Letterhead">
    <div class="wordmark"><span class="name">Bayfield</span><span class="sub">Tools and Building Materials Inc.</span></div>
    <div class="letter-body">
      <p>Bayfield Tools and Building Materials supplies hand tools, power tools, fasteners, lumber and finishing goods to homeowners, hobby builders and contractors across Metro Manila. Our counter staff help customers pick the right part, cut stock to size and plan each job before work begins.</p>
      <h3>Home projects</h3>
      <p>Weekend builders find paint, tile, plumbing fittings and garden tools on open shelves, with simple guides for repairs, shelving and small renovations.</p>
      <h3>Contractor accounts</h3>
      <p>Construction firms can open trade accounts with volume pricing, scheduled deliveries to site and monthly statements. Orders placed before noon are loaded and dispatched the same working day, and our yard keeps cement, steel bars and plywood in stock year round.</p>
      <h3>Tool rental</h3>
      <p>Mixers, grinders, ladders and scaffolding are available by the day or week, checked and serviced after every return.</p>
      <h3>Delivery</h3>
      <p>Trucks cover Manila, Quezon City and nearby towns six days a week. Site drops can be booked by phone or online, and drivers unload at the gate or the floor you name.</p>
      <h3>Workshops</h3>
      <p>Free Saturday classes teach safe tool use, basic wiring, tiling and carpentry for first-time builders, with materials supplied by the store.</p>
      <h3>Service and returns</h3>
      <p>Every item carries our store warranty. Bring the receipt within thirty days for an exchange, and ask our staff about repair support for power tools bought in store.</p>
    </div>
    <div class="letter-footer">www.btm-ph.com</div>
  </section>

  <section class="sheet card card-front" aria-label="Business card front">
    <div class="wordmark"><span class="name">Bayfield</span><span class="sub">Tools and Building Materials Inc.</span></div>
  </section>

  <section class="sheet card card-back" aria-label="Business card back">
    <div class="person">
      <div class="person-name">Marco Reyes</div>
      <div class="person-role">Co-Founder &amp; CEO</div>
    </div>
    <div class="wordmark"><span class="name">Bayfield</span><span class="sub">Tools and Building Materials Inc.</span></div>
    <ul class="contact">
      <li>T:&nbsp; (02) 846-1937</li>
      <li>M:&nbsp; bayfieldtools@mailbay.com</li>
      <li>W:&nbsp; www.btm-ph.com</li>
    </ul>
  </section>

  <section class="sheet envelope-front" aria-label="Envelope front">
    <div class="wordmark"><span class="name">Bayfield</span><span class="sub">Tools and Building Materials Inc.</span></div>
    <div class="address-window">
      <svg width="150" height="74" viewBox="0 0 150 74">
        <g stroke="var(--ink-line)" stroke-width="1">
          <line x1="17" y1="40" x2="134" y2="40"/>
          <line x1="17" y1="48" x2="134" y2="48"/>
          <line x1="17" y1="56" x2="134" y2="56"/>
          <line x1="17" y1="64" x2="134" y2="64"/>
        </g>
      </svg>
    </div>
  </section>

  <section class="sheet envelope-back" aria-label="Envelope back">
    <svg width="369" height="183" viewBox="0 0 369 183">
      <path d="M3 2 L3 40 Q3 52 16 54 L353 54 Q366 52 366 40 L366 2" fill="var(--brand-light)" fill-opacity="0.25" stroke="var(--brand-dark)" stroke-width="1"/>
    </svg>
  </section>

  <section class="sheet notepad" aria-label="Notepad cover">
    <div class="wordmark"><span class="name">Bayfield</span><span class="sub">Tools and Building Materials Inc.</span></div>
  </section>
  <svg class="spiral" viewBox="0 0 250 40" aria-hidden="true">
    <g fill="none" stroke="var(--ring)" stroke-width="2">
      <ellipse cx="18" cy="20" rx="4" ry="11"/><ellipse cx="42" cy="20" rx="4" ry="11"/>
      <ellipse cx="66" cy="20" rx="4" ry="11"/><ellipse cx="90" cy="20" rx="4" ry="11"/>
      <ellipse cx="114" cy="20" rx="4" ry="11"/><ellipse cx="138" cy="20" rx="4" ry="11"/>
      <ellipse cx="162" cy="20" rx="4" ry="11"/><ellipse cx="186" cy="20" rx="4" ry="11"/>
      <ellipse cx="210" cy="20" rx="4" ry="11"/><ellipse cx="234" cy="20" rx="4" ry="11"/>
    </g>
  </svg>

</body>
</html>
```